Business Card Design

we sell natural, organic & biological products. our brand includes fernavia - hair dye products, pluvensa-baby skin care and toothpaste... all products from Italy. our target customers are pharmacies, organic shops & stores, mum and baby care shops,.. i would love to see designs that use natural color, simple, friendly, eco concept.
Il ramo Verdino is Italian language, means Leafy branch, referring to the best parts on the top of wheat. The brands we carried currently are FernAvia Mielo and Pluvensa.

Target Market(s)

organic shops & store, pharmacies, mum n baby shops, bio/organic product users

Industry/Entity Type

Hair

Contact Information for Business Card

Marnie Koh WeiTing
Sales Manager
Il Ramo Verdino Singapore
Blk 318 Fernvale Crescent9
#07-12 Singapore 684217
Tel +65 6831 4072 Mobile +65 87246390
Reg No 48270315K
www.facebook.com/ilramoverdinosg

Requirements
Must have
• The front of the card should have my name, followed by my job title, my email address. Then the office address (company reg no), office tel, mobile phone.

My namecard should have all the brands my company carries.
Like ‘Pluvensa’, ‘Fernavia mielo’. Should have the brand logos too. This should be stated clearly at the back of the card. I will upload 'Fernavia' logo once I have it.

```html
<!DOCTYPE html>
<html lang="en">
<head>
<meta charset="utf-8">
<title>Il Ramo Verdino – Business Card</title>
<link rel="stylesheet" href="https://fonts.googleapis.com/css2?family=Cinzel:wght@400;600&family=Roboto+Condensed:ital,wght@0,400;0,700;1,400&display=swap">
<style>
  :root {
    --bg: #ececec;
    --paper: #ffffff;
    --brown: #553720;
    --amber: #e8923a;
    --shadow: rgba(0,0,0,0.18);
  }
  * { box-sizing: border-box; margin: 0; padding: 0; }
  html, body { width: 1200px; height: 947px; overflow: hidden; }
  body {
    background: var(--bg);
    position: relative;
    font-family: "Roboto Condensed", sans-serif;
  }
  .card {
    position: absolute;
    width: 520px;
    height: 300px;
    box-shadow: 0 10px 24px var(--shadow);
    overflow: hidden;
  }
  /* Front */
  .card--front {
    left: 50px; top: 323px;
    background: var(--paper);
    border-top: 10px solid var(--brown);
    border-bottom: 10px solid var(--brown);
    color: var(--brown);
  }
  .front__company {
    position: absolute; left: 36px; top: 24px;
    font-weight: 700; font-size: 24px; letter-spacing: 0.3px;
  }
  .front__role {
    position: absolute; left: 36px; top: 54px;
    font-style: italic; font-size: 17px;
  }
  .contact {
    position: absolute; left: 22px; top: 106px;
    list-style: none;
    font-weight: 700; font-size: 13.5px; line-height: 17px;
  }
  .contact li { display: flex; align-items: center; gap: 8px; white-space: nowrap; }
  .contact svg { width: 11px; height: 11px; flex: none; fill: var(--brown); }
  .contact .no-icon { width: 11px; flex: none; }
  .front__mark {
    position: absolute; right: 34px; bottom: 40px;
    display: flex; align-items: center; gap: 10px;
    font-weight: 700; font-size: 20px; color: var(--brown);
  }
  .front__mark .dot {
    width: 18px; height: 18px; border-radius: 50%; background: var(--brown);
  }
  /* Back */
  .card--back {
    left: 630px; top: 323px;
    background: var(--brown);
    color: var(--amber);
    font-family: "Cinzel", serif;
  }
  .back__mark {
    position: absolute; left: 0; right: 0; top: 62px;
    display: flex; justify-content: center; align-items: center; gap: 10px;
    font-size: 18px; font-weight: 600;
  }
  .back__mark .dot { width: 14px; height: 14px; border-radius: 50%; background: var(--amber); }
  .back__name {
    position: absolute; left: 0; right: 0; top: 108px;
    text-align: center; font-size: 26px; letter-spacing: 1px;
  }
  .back__title {
    position: absolute; left: 0; right: 0; top: 146px;
    text-align: center; font-size: 14px; letter-spacing: 1.5px;
  }
  .brands {
    position: absolute; left: 0; right: 0; top: 212px;
    display: flex; justify-content: center; gap: 48px;
    list-style: none;
    font-size: 15px; font-weight: 600; letter-spacing: 1px;
  }
  .brands li { display: flex; align-items: center; gap: 8px; }
  .brands .square { width: 12px; height: 12px; background: var(--amber); }
</style>
</head>
<body>
  <section class="card card--front" aria-label="Card front">
    <div class="front__company">Il Ramo Verdino&nbsp; SG</div>
    <div class="front__role">Sales Manager</div>
    <ul class="contact">
      <li><svg viewBox="0 0 12 12"><path d="M6 1 0.5 6H2v5h3V8h2v3h3V6h1.5z"/></svg>Blk 318 Fernvale Cres 9 #07-12 Singapore 684217</li>
      <li><svg viewBox="0 0 12 12"><path d="M2.5 1h2l1 3-1.5 1a6 6 0 0 0 3 3l1-1.5 3 1v2c0 .6-.5 1-1 1A9.5 9.5 0 0 1 1.5 2c0-.5.4-1 1-1z"/></svg>65 6831 4072</li>
      <li><svg viewBox="0 0 12 12"><path d="M3.5 0h5a1 1 0 0 1 1 1v10a1 1 0 0 1-1 1h-5a1 1 0 0 1-1-1V1a1 1 0 0 1 1-1zm.5 1.5v7.5h4V1.5z"/></svg>65 87246390</li>
      <li><span class="no-icon"></span>Reg No 48270315K</li>
      <li><svg viewBox="0 0 12 12"><rect width="12" height="12" rx="1.5"/></svg>/ilramoverdinosg</li>
    </ul>
    <div class="front__mark"><span class="dot"></span>Il Ramo Verdino</div>
  </section>

  <section class="card card--back" aria-label="Card back">
    <div class="back__mark"><span class="dot"></span>Il Ramo Verdino</div>
    <div class="back__name">Marnie/Koh WeiTing</div>
    <div class="back__title">Sales Manager</div>
    <ul class="brands" aria-label="Brands carried">
      <li><span class="square"></span>Fernavia Mielo</li>
      <li><span class="square"></span>Pluvensa</li>
    </ul>
  </section>
</body>
</html>
```